Party business requiring flyer and logo

Create a flyer (to be used online and offline) to promote a new business name for our business we are re-branding.
Business name
Hopscotch Fun and Games
Concept
# Birthday party room
# Parties that incorporate party room and full size basketball court
# Suitable for all ages, including adult parties
# Also available for hire by parent groups of young children to play
Facilities:
# General play space
# Full size basketball court
# Ball pit
# Portable soccer goal/reduced size basketball ring
# Movies
Catering and decorating packages available.
Private space, exclusive hire.
Catering to a large number of party themes.
Kitchen facilities available
Party host options
Note - we also require a new logo for this re-branding. We think about possibly keeping a similar look to the old logo with possibly replacing the A for a party hat etc. Happy to see whatever you come up with.
Existing business is called Redgum Athletics, a basketball training and development facility. The new business needs to be linked to Redgum Athletics from a banding perspective although does require its own identity
Brand essence - fun, vibrant, colourful, engaging
Industry/Entity Type
Entertainment
Logo Text
Hopscotch Fun and Games
Font styles to use
Colors
Designer to choose colors to be used in the design.
Requirements
Must have
- Must Have:
- - Must be vibrant, colourful and fun
- - Get across sense of energy
- - Our predominant market is children's parties however also needs to be relevant to adult parties also
Nice to have
- Contact details:
- Phone - 0472 951 306
- Email - lindap@redgumathletics.example.com.au
- Web - www.hopscotchfunandgames.example.com.au
Should not have
- Pricing
- Too specific details this will be a general flyer outlining briefly what we do without pigeon-holing us into a specific theme/category

```html
<!DOCTYPE html>
<html lang="en">
<head>
<meta charset="utf-8">
<title>Hopscotch Fun and Games – Party Venue Flyer</title>
<link rel="stylesheet" href="https://fonts.googleapis.com/css2?family=Bowlby+One+SC&family=Lato:ital,wght@0,400;0,700;1,400&display=swap">
<style>
  :root{
    --page:#ecebe8;
    --paper:#ffffff;
    --ink:#222222;
    --purple:#8e1f8f;
    --blue:#1a5fb4;
    --pink:#e8178a;
    --orange:#f28c1a;
    --red:#ee5a24;
    --green:#3aa935;
    --dark:#2f2f30;
    --gold:#f5a623;
  }
  *{margin:0;padding:0;box-sizing:border-box}
  html,body{width:1200px;height:1200px;overflow:hidden;background:var(--page)}
  .flyer{
    position:absolute;left:152px;top:20px;width:896px;height:1160px;
    background:var(--paper);overflow:hidden;
    box-shadow:0 6px 24px rgba(0,0,0,.18);
    font-family:'Lato',sans-serif;color:var(--ink);
  }
  .flyer-shapes{position:absolute;inset:0}
  .brand{position:absolute;left:52px;top:82px;font-family:'Bowlby One SC',sans-serif;font-weight:400;line-height:1;color:var(--purple)}
  .brand-name{font-size:50px;display:flex;align-items:center;gap:12px}
  .brand-dot{width:24px;height:24px;border-radius:50%;background:var(--orange);display:inline-block}
  .brand-tag{font-size:29px;margin-top:12px}
  .headline{position:absolute;left:52px;top:366px;font-family:'Bowlby One SC',sans-serif;font-weight:400;line-height:1}
  .headline-top{color:var(--purple);font-size:33px}
  .headline-main{color:var(--blue);font-size:46px;margin-top:12px}
  .facilities-tab{
    position:absolute;left:0;top:489px;width:226px;height:36px;
    background:var(--pink);border-radius:0 12px 12px 0;
    color:#fff;font-size:21px;font-weight:700;padding-left:52px;line-height:36px;
  }
  .facilities{position:absolute;left:50px;top:546px;list-style:none;font-size:15px}
  .facility{display:flex;align-items:flex-start;gap:14px;min-height:31px;margin-bottom:1px}
  .facility svg{width:28px;height:24px;flex:none}
  .facility span{padding-top:3px;line-height:1.25}
  .contact{position:absolute;right:50px;top:1018px;text-align:right;color:#fff}
  .contact-call{color:var(--gold);font-style:italic;font-size:25px;margin-right:-6px}
  .contact-line{display:flex;justify-content:flex-end;align-items:center;gap:8px}
  .contact-phone{font-size:20px;font-weight:700;margin-top:6px}
  .contact-small{font-size:13px;margin-top:5px}
  .contact-line svg{width:16px;height:16px;flex:none}
</style>
</head>
<body>
<main class="flyer">
  <svg class="flyer-shapes" viewBox="0 0 896 1160">
    <defs>
      <linearGradient id="washLeft" x1="0" y1="0" x2="1" y2="0">
        <stop offset="0" stop-color="#f3f2f6"/>
        <stop offset="1" stop-color="#ffffff"/>
      </linearGradient>
      <linearGradient id="partyBase" x1="0" y1="0" x2="1" y2="0">
        <stop offset="0" stop-color="#ffffff" stop-opacity="0"/>
        <stop offset="0.3" stop-color="#f6e2d6"/>
        <stop offset="0.55" stop-color="#d99a78"/>
        <stop offset="0.8" stop-color="#a65c45"/>
        <stop offset="1" stop-color="#c2704c"/>
      </linearGradient>
      <radialGradient id="partyGlow" cx="0.7" cy="0.5" r="0.5">
        <stop offset="0" stop-color="#f0b26a" stop-opacity=".85"/>
        <stop offset="0.5" stop-color="#e06a7a" stop-opacity=".35"/>
        <stop offset="1" stop-color="#e06a7a" stop-opacity="0"/>
      </radialGradient>
      <radialGradient id="partyShade" cx="0.55" cy="0.85" r="0.45">
        <stop offset="0" stop-color="#4a2a2a" stop-opacity=".55"/>
        <stop offset="1" stop-color="#4a2a2a" stop-opacity="0"/>
      </radialGradient>
      <linearGradient id="kidsFade" x1="0" y1="0" x2="1" y2="0">
        <stop offset="0" stop-color="#ffffff" stop-opacity="0"/>
        <stop offset="0.25" stop-color="#f1e6dd"/>
        <stop offset="1" stop-color="#efe3d8"/>
      </linearGradient>
      <linearGradient id="kidsBody" x1="0" y1="0" x2="0" y2="1">
        <stop offset="0" stop-color="#d9a784" stop-opacity="0"/>
        <stop offset="0.3" stop-color="#c68f6b"/>
        <stop offset="0.5" stop-color="#2b2b2d"/>
        <stop offset="1" stop-color="#1f1f21"/>
      </linearGradient>
      <radialGradient id="ballGlow" cx="0.5" cy="0.5" r="0.5">
        <stop offset="0" stop-color="#d77a48"/>
        <stop offset="1" stop-color="#d77a48" stop-opacity="0"/>
      </radialGradient>
      <linearGradient id="venueA" x1="0" y1="0" x2="0" y2="1">
        <stop offset="0" stop-color="#3a3436"/>
        <stop offset="0.35" stop-color="#c8a88a"/>
        <stop offset="0.6" stop-color="#e0384c"/>
        <stop offset="0.8" stop-color="#3b4fa6"/>
        <stop offset="1" stop-color="#4f9a3c"/>
      </linearGradient>
      <linearGradient id="venueB" x1="0" y1="0" x2="0" y2="1">
        <stop offset="0" stop-color="#d27ad8"/>
        <stop offset="0.35" stop-color="#3a3a40"/>
        <stop offset="0.6" stop-color="#3aa0d8"/>
        <stop offset="0.8" stop-color="#2f4aa0"/>
        <stop offset="1" stop-color="#5aa044"/>
      </linearGradient>
    </defs>

    <rect x="0" y="300" width="896" height="800" fill="url(#washLeft)"/>

    <g role="img" aria-label="Photo: group of young adults laughing and celebrating a 30th birthday with a cake and confetti">
      <polygon points="120,0 896,0 896,474 702,518 192,288 120,316" fill="url(#partyBase)"/>
      <polygon points="120,0 896,0 896,474 702,518 192,288 120,316" fill="url(#partyGlow)"/>
      <polygon points="120,0 896,0 896,474 702,518 192,288 120,316" fill="url(#partyShade)"/>
    </g>

    <g class="colour-stripe" stroke-width="8" fill="none">
      <line x1="0" y1="364" x2="96" y2="327" stroke="#1a5fb4"/>
      <line x1="96" y1="327" x2="192" y2="290" stroke="#3aa935"/>
      <line x1="192" y1="290" x2="294" y2="336" stroke="#f28c1a"/>
      <line x1="294" y1="336" x2="396" y2="382" stroke="#e8178a"/>
      <line x1="396" y1="382" x2="498" y2="428" stroke="#8e1f8f"/>
      <line x1="498" y1="428" x2="600" y2="474" stroke="#1a5fb4"/>
      <line x1="600" y1="474" x2="702" y2="520" stroke="#3aa935"/>
      <line x1="702" y1="520" x2="799" y2="498" stroke="#f28c1a"/>
      <line x1="799" y1="498" x2="896" y2="476" stroke="#ee5a24"/>
    </g>

    <g role="img" aria-label="Photo: three smiling boys in black sports tops, one holding a basketball">
      <rect x="380" y="560" width="516" height="420" fill="url(#kidsFade)"/>
      <path d="M470 980 C470 760 520 640 640 610 C760 590 860 640 896 700 L896 980 Z" fill="url(#kidsBody)"/>
      <circle cx="615" cy="810" r="70" fill="url(#ballGlow)"/>
    </g>

    <polygon points="0,1086 896,940 896,952 0,1098" fill="var(--red)"/>
    <polygon points="0,1098 896,952 896,1160 0,1160" fill="var(--dark)"/>

    <circle cx="383" cy="1017" r="107" fill="url(#venueB)" role="img" aria-label="Photo: children at a party table in the play venue with balloons"/>
    <circle cx="383" cy="1017" r="107" fill="none" stroke="var(--pink)" stroke-width="8"/>
    <circle cx="181" cy="1006" r="129" fill="url(#venueA)" role="img" aria-label="Photo: children seated at a red party table on artificial grass"/>
    <circle cx="181" cy="1006" r="129" fill="none" stroke="var(--orange)" stroke-width="8"/>
    <circle cx="181" cy="1006" r="119" fill="none" stroke="var(--purple)" stroke-width="1.5"/>
  </svg>

  <header class="brand">
    <div class="brand-name">Hopscotch <i class="brand-dot"></i></div>
    <div class="brand-tag">Fun and Games</div>
  </header>

  <h1 class="headline">
    <div class="headline-top">Your exclusive</div>
    <div class="headline-main">Party Venue!</div>
  </h1>

  <h2 class="facilities-tab">Our Facilities</h2>

  <ul class="facilities">
    <li class="facility"><svg viewBox="0 0 28 24"><circle cx="18" cy="4" r="3" fill="#1a5fb4"/><path d="M18 8v8l-4 6M18 16l4 6M12 10l6-1 5 3" stroke="#1a5fb4" stroke-width="2" fill="none"/></svg><span>General play space</span></li>
    <li class="facility"><svg viewBox="0 0 28 24"><rect x="2" y="5" width="24" height="14" fill="none" stroke="#8e1f8f" stroke-width="1.6"/><line x1="14" y1="5" x2="14" y2="19" stroke="#8e1f8f" stroke-width="1.6"/><circle cx="14" cy="12" r="3" fill="none" stroke="#8e1f8f" stroke-width="1.6"/></svg><span>Full size basketball court</span></li>
    <li class="facility"><svg viewBox="0 0 28 24"><circle cx="14" cy="12" r="10" fill="none" stroke="#3aa935" stroke-width="2"/><polygon points="14,8 18,11 16.5,16 11.5,16 10,11" fill="#3aa935"/></svg><span>Ball pit</span></li>
    <li class="facility"><svg viewBox="0 0 28 24"><rect x="3" y="2" width="22" height="12" rx="2" fill="none" stroke="#ee5a24" stroke-width="2"/><path d="M9 12h10l-2 10h-6z" fill="none" stroke="#ee5a24" stroke-width="1.6"/></svg><span>Portable soccer goal/reduced size<br>basketball ring</span></li>
    <li class="facility"><svg viewBox="0 0 28 24"><rect x="2" y="4" width="24" height="16" fill="#e8178a"/><rect x="4" y="6" width="3" height="2" fill="#fff"/><rect x="10" y="6" width="3" height="2" fill="#fff"/><rect x="16" y="6" width="3" height="2" fill="#fff"/><rect x="22" y="6" width="3" height="2" fill="#fff"/><rect x="4" y="16" width="3" height="2" fill="#fff"/><rect x="10" y="16" width="3" height="2" fill="#fff"/><rect x="16" y="16" width="3" height="2" fill="#fff"/><rect x="22" y="16" width="3" height="2" fill="#fff"/></svg><span>Movies</span></li>
    <li class="facility"><svg viewBox="0 0 28 24"><path d="M5 2l18 20M23 2L5 22" stroke="#3aa935" stroke-width="2.5"/></svg><span>Catering and decorating packages available</span></li>
    <li class="facility"><svg viewBox="0 0 28 24"><ellipse cx="14" cy="12" rx="11" ry="6" fill="none" stroke="#1a5fb4" stroke-width="1.8"/><circle cx="14" cy="12" r="3" fill="#1a5fb4"/><line x1="4" y1="3" x2="24" y2="21" stroke="#1a5fb4" stroke-width="1.8"/></svg><span>Private space, exclusive hire</span></li>
    <li class="facility"><svg viewBox="0 0 28 24"><path d="M4 14h20a10 10 0 0 1-20 0z" fill="#8e1f8f"/><path d="M9 3v5M14 2v5M19 3v5" stroke="#8e1f8f" stroke-width="1.8"/></svg><span>Catering to a large number of party themes</span></li>
    <li class="facility"><svg viewBox="0 0 28 24"><rect x="2" y="5" width="24" height="14" rx="2" fill="none" stroke="#8e1f8f" stroke-width="1.6"/><circle cx="9" cy="12" r="3" fill="none" stroke="#8e1f8f" stroke-width="1.6"/><circle cx="19" cy="12" r="3" fill="none" stroke="#8e1f8f" stroke-width="1.6"/></svg><span>Kitchen facilities available</span></li>
    <li class="facility"><svg viewBox="0 0 28 24"><circle cx="14" cy="5" r="3" fill="#1a5fb4"/><path d="M14 9v8l-4 6M14 17l4 6M7 8l7 3 7-3" stroke="#1a5fb4" stroke-width="2" fill="none"/></svg><span>Party host options</span></li>
  </ul>

  <section class="contact">
    <p class="contact-call">Call us now to enquire!</p>
    <p class="contact-line contact-phone">0472 951 306
      <svg viewBox="0 0 16 16"><path d="M4 1l3 3-2 2a9 9 0 0 0 5 5l2-2 3 3-2 3C7 15 1 9 1 3z" fill="none" stroke="var(--gold)" stroke-width="1.5"/></svg></p>
    <p class="contact-line contact-small">lindap@redgumathletics.example.com.au
      <svg viewBox="0 0 16 16"><rect x="1" y="4" width="14" height="9" fill="var(--gold)"/><path d="M1 4l7 5 7-5" stroke="#2f2f30" stroke-width="1.2" fill="none"/></svg></p>
    <p class="contact-line contact-small">www.hopscotchfunandgames.example.com.au
      <svg viewBox="0 0 16 16"><circle cx="8" cy="8" r="6.5" fill="none" stroke="var(--gold)" stroke-width="1.5"/><ellipse cx="8" cy="8" rx="3" ry="6.5" fill="none" stroke="var(--gold)" stroke-width="1.2"/><line x1="1.5" y1="8" x2="14.5" y2="8" stroke="var(--gold)" stroke-width="1.2"/></svg></p>
  </section>
</main>
</body>
</html>
```